Business card design for modern law firm

We need new business cards. Information about our law firm can be found at www.qrtl-recht.de. The business cards should include the information that we have offices in Berlin and Stuttgart. They should be customizable for all attorneys who are partially located in Berlin and partially in Stuttgart. Example of the information:
Jonas Ackermann
lawyer
Specialist lawyer for copyright and media law
Lindenweg 17, 70374 Stuttgart
ackermann@qrtl-recht.de
+49 711 483 15 260
www.qrtl-recht.de
It is important for us that we can edit the cards independently, i.e. exchange names and contact details.
In addition, a QR code for a VCard should be placed on the card.
The design of the old maps is attached; the new design should clearly distinguish itself from them. They should be more modern. The design is ideally based on the design of the website www.qrtl-recht.de.
Industry/Entity Type
Rechtsanwalt
Contact Information for Business Card
Siehe projektbeschreibung

```html
<!DOCTYPE html>
<html lang="de">
<head>
<meta charset="utf-8">
<title>qrtl Rechtsanwälte – Visitenkarte</title>
<link rel="stylesheet" href="https://fonts.googleapis.com/css2?family=Montserrat:wght@300;400&family=Open+Sans:wght@400;700&family=Roboto+Slab:wght@500&display=swap">
<style>
  :root {
    --page: #ffffff;
    --sage: #adc096;
    --sage-light: #c6d4b6;
    --paper: #f2f5ee;
    --paper-tile: #dfe8d6;
    --lime: #a4cc3a;
    --grey: #7d7d7d;
    --ink: #111111;
    --white: #ffffff;
    --tower-front: #e9efe2;
    --tower-back: #b8c7a6;
  }
  * { margin: 0; padding: 0; box-sizing: border-box; }
  html, body { width: 1200px; height: 1200px; overflow: hidden; background: var(--page); }
  .canvas { position: relative; width: 1200px; height: 1200px; }

  .card { position: absolute; left: 309px; width: 582px; height: 340px; overflow: hidden; }
  .card--front { top: 245px; background: var(--sage); }
  .card--back { top: 615px; background: var(--paper); }

  .tile-field { position: absolute; left: 0; top: 0; }

  .city { position: absolute; font-family: "Montserrat", sans-serif; font-weight: 400; font-size: 15px; color: var(--white); letter-spacing: 0.3px; }
  .city--berlin { left: 285px; top: 100px; }
  .city--stuttgart { left: 333px; top: 122px; }

  .towers { position: absolute; left: 264px; top: 105px; width: 70px; height: 235px; border-radius: 6px 6px 0 0;
    background: linear-gradient(180deg, rgba(255,255,255,0.05), rgba(255,255,255,0.35)); }

  .wordmark { position: absolute; font-family: "Montserrat", sans-serif; font-weight: 300; color: var(--lime); line-height: 1; letter-spacing: 1px; }
  .wordmark--front { left: 394px; top: 148px; font-size: 54px; }
  .wordmark--back { left: 228px; top: 92px; font-size: 44px; }

  .firm { position: absolute; left: 338px; top: 92px; font-family: "Roboto Slab", serif; font-weight: 500; }
  .firm__title { display: block; font-size: 15.5px; letter-spacing: 3.6px; color: var(--lime); }
  .firm__sub { display: block; margin-top: 4px; font-size: 11.5px; letter-spacing: 1.8px; color: var(--grey); }
  .firm__sub small { font-size: 9.5px; letter-spacing: 1px; }

  .tower-strip { position: absolute; left: 245px; top: 156px; width: 10px; height: 153px;
    background: linear-gradient(180deg, rgba(164,204,58,0.15), rgba(164,204,58,0.55)); }

  .contact { position: absolute; left: 259px; top: 176px; font-family: "Open Sans", sans-serif; font-size: 12.5px; line-height: 15.6px; color: var(--ink); }
  .contact__name { font-weight: 700; }
  .contact__gap { height: 15.6px; }

  .icons { position: absolute; left: 230px; top: 240px; }
  .baseline { position: absolute; left: 0; top: 309px; width: 256px; height: 1px; background: #c7d4ba; }
</style>
</head>
<body>
<main class="canvas">

  <section class="card card--front" aria-label="Vorderseite">
    <svg class="tile-field" width="320" height="270" viewBox="0 0 320 270" aria-hidden="true">
      <defs>
        <linearGradient id="tileFront" x1="0" y1="0" x2="1" y2="1">
          <stop offset="0" stop-color="#c6d4b6"/>
          <stop offset="1" stop-color="#b7c8a3"/>
        </linearGradient>
      </defs>
      <polygon fill="url(#tileFront)" points="0,0 311,0 311,44 267,44 267,89 178,89 178,133 133,133 133,178 89,178 89,222 44,222 44,267 0,267"/>
    </svg>
    <span class="city city--berlin">Berlin</span>
    <span class="city city--stuttgart">Stuttgart</span>
    <div class="towers" role="img" aria-label="Linienzeichnung des Berliner Fernsehturms und des Stuttgarter Fernsehturms"></div>
    <div class="wordmark wordmark--front">qrtl</div>
  </section>

  <section class="card card--back" aria-label="Rückseite">
    <svg class="tile-field" width="280" height="270" viewBox="0 0 280 270" aria-hidden="true">
      <defs>
        <linearGradient id="tileBack" x1="0" y1="0" x2="1" y2="1">
          <stop offset="0" stop-color="#dfe8d6"/>
          <stop offset="1" stop-color="#e8eee2"/>
        </linearGradient>
      </defs>
      <polygon fill="url(#tileBack)" points="0,0 266,0 266,44 222,44 222,89 133,89 133,133 89,133 89,178 89,178 89,222 44,222 44,267 0,267"/>
    </svg>

    <div class="wordmark wordmark--back">qrtl</div>
    <div class="firm">
      <span class="firm__title">RECHTSANWÄLTE</span>
      <span class="firm__sub">LEGAL SERVICES <small>PartmbB</small></span>
    </div>

    <div class="tower-strip" role="img" aria-label="Schmale Zeichnung des Stuttgarter Fernsehturms"></div>

    <svg class="icons" width="14" height="64" viewBox="0 0 14 64" fill="none" stroke="#b9c4ae" stroke-width="1" aria-hidden="true">
      <path d="M7 11 C3 6 3.5 2 7 1.5 C10.5 2 11 6 7 11 Z"/><circle cx="7" cy="5" r="1.4"/>
      <rect x="2" y="20" width="10" height="7"/><path d="M2 20 L7 24 L12 20"/>
      <path d="M3 36 C3 40 7 43 10 43 L11 41 L9 39.5 L8 40.5 C6.5 40 5 38.5 4.5 37 L5.5 36 L4 34 Z"/>
      <circle cx="7" cy="56" r="4.5"/><path d="M2.5 56 H11.5 M7 51.5 C5 54 5 58 7 60.5 M7 51.5 C9 54 9 58 7 60.5"/>
    </svg>

    <div class="contact">
      <div class="contact__name">Jonas Ackermann</div>
      <div>lawyer</div>
      <div>Specialist lawyer for copyright and media law</div>
      <div class="contact__gap"></div>
      <div>Lindenweg 17, 70374 Stuttgart</div>
      <div>ackermann@qrtl-recht.de</div>
      <div>+49 711 483 15 260</div>
      <div>www.qrtl-recht.de</div>
    </div>

    <div class="baseline"></div>
  </section>

</main>
</body>
</html>
```